Marrowick Off-Grid Energy

The company provides world wide installations and products for off-grid energy solutions. This means AC power where there is no network available. Mostly this is with solar panels combined with hybrid inverters and Lithium batteries. In the future small windmills and hydropower. The company is Dutch but has a hub in Hungary to supply the Balkan and surrounding countries.

We sell all Tovu products and also Pyramoxa and Quillbrook energy products

I have 3 versions of my logo. 2 attached and the third is the Off-grid energy text in black. Just see what works best with the design.
Obviously I need a good design but also good coding. It needs to meet al the latest (Google) search engine standards and should heave a web shop.
The web shop should be able to work with different currencies and calculate international shipping fees. Orders should be paid with; credit card, Coinwisp, Faxo or whatever is used internationally.

Coding

Coded - Design and coding required

Number of Pages Required

5+ page

Font styles to use
Other font styles liked:
• see logo

Colors
0054AA
0677BA
7BADD7
CADEEF
E8F1F8
0094D4
00A9DD
6FCCEA
C7EBF8
E9F6FB
59FF00
82FF00
B8FF75
E3FFCB
F4FFEA
EB3D1F
EC4F4E
F09395
F8D3D4
FCEDEE

Requirements
Must have
• web shop
Nice to have
• slick design
Should not have
• stupid things ;-)

```html
<!DOCTYPE html>
<html lang="en">
<head>
<meta charset="utf-8">
<title>Marrowick Off-Grid Energy – Home</title>
<link rel="stylesheet" href="https://fonts.googleapis.com/css2?family=Manrope:wght@400;500;600;700;800&display=swap">
<style>
:root{
  --lime:#8cff2e;
  --lime-bg:#a8ff66;
  --lime-soft:#c2ff8e;
  --orange:#ff4a1c;
  --blue:#4a5cff;
  --ink:#16181d;
  --muted:#7b808a;
  --line:#dfe2e6;
  --paper:#f7f8f9;
  --paper-2:#f1f3f6;
  --canvas:#e6e8eb;
}
*{box-sizing:border-box;margin:0;padding:0}
html,body{width:1200px;height:1200px;overflow:hidden}
body{background:var(--canvas);font-family:"Manrope",sans-serif;color:var(--ink);position:relative}
.page-col{position:absolute;top:33px;width:493px;background:#fff;box-shadow:0 6px 24px rgba(0,0,0,.08);overflow:hidden}
.col-a{left:72px}
.col-b{left:635px}
.photo{position:absolute}
.eyebrow{font-size:4.5px;letter-spacing:.18em;font-weight:700;text-transform:uppercase}
.btn{display:inline-block;background:var(--orange);color:#fff;font-size:4.5px;font-weight:700;padding:5px 11px}

/* hero */
.hero{position:relative;height:224px;overflow:hidden}
.hero .photo{inset:0;background:linear-gradient(180deg,#8fa6bf 0%,#a9b3b7 30%,#6d7768 55%,#4e5a45 80%,#3c4536 100%)}
.nav{position:absolute;top:10px;left:18px;right:18px;display:flex;align-items:center;font-size:4.2px;color:#fff}
.brand{font-weight:800;font-size:9px;letter-spacing:-.01em;display:flex;align-items:center;gap:3px}
.brand i{width:6px;height:6px;background:var(--lime);display:block}
.nav-links{display:flex;gap:10px;margin-left:82px}
.nav-links span:first-child{border-bottom:1px solid #fff}
.lang{margin-left:auto;background:#fff;color:var(--ink);padding:2px 5px;font-weight:700}
.nav .btn{margin-left:18px;padding:3px 8px}
.hero h1{position:absolute;left:18px;right:18px;top:100px;font-size:40px;line-height:42px;font-weight:700;letter-spacing:-.02em}
.hero h1 .l1{color:var(--lime);display:block}
.hero h1 .l2{color:#fff;display:block;text-align:right}
.hero p{position:absolute;left:18px;top:160px;width:128px;font-size:4px;line-height:6.5px;color:#e8ece6}

/* sources */
.sources{height:292px;background:var(--paper);text-align:center;padding-top:30px}
.sources h2{color:var(--lime);font-size:15px;line-height:15px;font-weight:700;margin-top:6px}
.source-list{display:flex;justify-content:center;gap:24px;margin-top:16px}
.source{width:90px}
.source .ic{width:27px;height:27px;border-radius:50%;background:#e7ecef;margin:0 auto;display:flex;align-items:center;justify-content:center}
.source h3{font-size:6px;font-weight:700;margin-top:10px}
.source p{font-size:3.8px;line-height:6px;color:var(--muted);margin-top:4px}
.source .arr{font-size:6px;margin-top:3px}
.partners{display:grid;grid-template-columns:repeat(4,82px);gap:7px 3px;justify-content:center;margin-top:30px}
.partners span{height:32px;border:1px solid var(--line);display:flex;align-items:center;justify-content:center;font-size:8px;font-weight:600;color:#a7acb3;background:#fff}

/* green growth */
.growth{position:relative;height:432px;background:var(--paper-2)}
.growth .worker{left:0;top:31px;width:246px;height:223px;background:linear-gradient(160deg,#7fb9e6 0%,#a9d3f0 45%,#c9d9a3 75%,#8aa06a 100%)}
.growth .copy{position:absolute;left:228px;top:90px;width:190px}
.growth h2{font-size:13px;line-height:15px;font-weight:600}
.growth .copy p{font-size:3.8px;line-height:6px;color:var(--muted);margin:10px 0 0 55px}
.growth .copy p+p{margin-top:6px}
.growth .btn{margin:12px 0 0 55px}
.growth .mill{right:0;top:230px;width:130px;height:202px;background:linear-gradient(180deg,#f1f3f6 0%,#c9ccc6 45%,#8f8a7a 75%,#6f7a52 100%);clip-path:polygon(60% 0,100% 8%,100% 100%,0 100%,20% 45%)}
.growth .mark{position:absolute;right:76px;top:235px;font-size:9px;font-weight:800;display:flex;align-items:center;gap:3px}
.growth .mark i{width:6px;height:6px;background:var(--lime);display:block}
.quote{position:absolute;left:130px;top:268px;width:236px;text-align:center}
.avatar{width:26px;height:26px;border-radius:50%;background:#3b3f45;margin:0 auto}
.quote p{font-size:5px;line-height:8px;margin-top:14px}
.quote .q{color:var(--blue);font-size:8px;margin-top:8px;font-weight:800}
.quote .who{font-size:4.2px;font-weight:700}
.quote .role{font-size:3.8px;color:var(--muted)}
.dots{display:flex;gap:3px;justify-content:center;margin-top:10px}
.dots i{width:3px;height:3px;border-radius:50%;background:#c9ccd1}
.dots i.on{background:var(--lime)}
.prev{position:absolute;left:80px;top:337px;width:12px;height:12px;border-radius:50%;border:1px solid var(--line);font-size:5px;display:flex;align-items:center;justify-content:center}

/* banner */
.banner{position:relative;height:186px;text-align:center}
.banner .photo{inset:0;background:linear-gradient(180deg,#6f9fd6 0%,#a9c4e2 30%,#7c6a5b 55%,#a2563f 75%,#5c6b3e 100%)}
.banner .inner{position:relative;padding-top:68px}
.banner .eyebrow{color:#fff;font-size:3.5px}
.banner h2{color:var(--orange);font-size:13px;line-height:14px;font-weight:600;margin-top:4px}
.banner .btn{margin-top:10px;padding:3px 10px}

/* pricing */
.offer{height:444px;background:var(--lime-bg);padding:32px 81px 0}
.offer h2{font-size:13px;line-height:15px;font-weight:700;margin-top:4px}
.offer .sub{font-size:3.8px;margin-top:6px}
.plans{display:flex;gap:7px;margin-top:16px}
.plan{width:106px;background:var(--orange);color:#fff;text-align:center;height:118px;position:relative;padding-top:18px}
.plan.mid{background:var(--lime-soft)}
.plan .name{font-size:4.5px;font-weight:700}
.plan .price{font-size:15px;font-weight:700;margin-top:6px}
.plan .per{font-size:3.5px;opacity:.8;margin-top:3px}
.plan .txt{font-size:3.5px;line-height:5.5px;opacity:.85;margin:14px 12px 0;text-align:left}
.plan.mid .rule{height:1px;background:#fff;opacity:.6;margin:12px 12px 0}
.plan .get{position:absolute;left:0;right:0;bottom:-14px;height:14px;background:#fff;color:var(--ink);font-size:3.8px;font-weight:700;line-height:14px}
.plan.mid .get{background:var(--blue);color:#fff}
.homes{position:relative;margin-top:46px;height:166px}
.homes .house{left:0;top:0;width:135px;height:166px;background:linear-gradient(170deg,#6da8e8 0%,#b8d6f2 35%,#4d4f58 55%,#8a5a45 80%,#6b7a4a 100%)}
.homes .tag{position:absolute;left:81px;top:104px;width:81px;height:62px;background:var(--ink);color:#fff;font-size:6.5px;font-weight:700;line-height:7.5px;padding:17px 0 0 10px}
.homes .copy{position:absolute;left:199px;top:22px;width:132px}
.homes h3{font-size:13px;line-height:14px;font-weight:700;margin-top:4px}
.homes p{font-size:3.8px;line-height:6px;margin-top:8px}
.homes ul{list-style:none;margin-top:6px}
.homes li{font-size:4px;border-bottom:1px solid rgba(0,0,0,.35);padding:6px 0;color:#fff;font-weight:600}
.homes li b{color:var(--ink);opacity:.5;margin-right:8px;font-weight:600}
.homes .white{display:inline-block;background:#fff;font-size:4px;font-weight:700;padding:4px 9px;margin-top:10px}

/* marquee */
.marquee{position:relative;height:216px;background:#fff;overflow:hidden}
.band{position:absolute;white-space:nowrap;font-weight:800;font-size:38px;letter-spacing:-.01em;transform-origin:left top}
.band-dark{color:var(--ink);left:-40px;top:136px;transform:rotate(-15deg)}
.band-lime{color:var(--lime);left:-40px;top:182px;transform:rotate(-15deg)}
.band em{font-style:normal;font-size:22px;margin:0 10px;vertical-align:middle}
.band .sq{display:inline-block;width:20px;height:14px;background:#1e3a6e;margin:0 12px;vertical-align:middle}

/* blog */
.blog{height:328px;background:var(--paper-2);text-align:center;padding-top:32px}
.blog h2{font-size:12px;line-height:14.5px;font-weight:600;margin:5px auto 0;width:280px}
.blog h2 u{color:#39c13a;text-decoration-thickness:1px}
.blog .sig{font-size:4px;font-weight:700;margin-top:10px}
.blog .sig span{display:block;font-weight:400;color:var(--muted);font-size:3.5px;margin-top:2px}
.posts{display:flex;gap:7px;justify-content:center;margin-top:18px;text-align:left;align-items:flex-start}
.post{width:106px}
.post .thumb{position:static;height:72px}
.post:nth-child(1) .thumb{background:linear-gradient(180deg,#8fc4ef 0%,#c7e1f3 45%,#6fa84d 70%,#4e7d36 100%)}
.post:nth-child(2) .thumb{height:106px;background:linear-gradient(135deg,#5a3b2b 0%,#8a6048 45%,#6c4a36 100%)}
.post:nth-child(3) .thumb{height:72px;background:linear-gradient(180deg,#c9d4dc 0%,#dfe3e0 40%,#8b7a5f 70%,#6e5c44 100%)}
.post:nth-child(1){margin-top:0}
.post:nth-child(3){margin-top:0}
.post .meta{font-size:3px;color:var(--muted);margin-top:8px;padding-left:12px;position:relative}
.post .meta::before{content:"";position:absolute;left:0;top:1.5px;width:8px;height:1px;background:var(--ink)}
.post h4{font-size:5.5px;line-height:7px;font-weight:600;margin-top:3px;padding-left:12px}

/* footer */
.footer{height:149px;background:var(--orange);padding:34px 81px 0;color:#fff}
.social{display:flex;gap:9px}
.social i{width:3px;height:3px;border-radius:50%;background:#fff;display:block;opacity:.85}
.footer h2{font-size:12px;line-height:14.5px;font-weight:600;margin-top:30px}
.footer h2 .dim{color:#ffb09a}
.footer h2 u{text-decoration-thickness:1px}
.footer small{display:block;font-size:3.8px;margin-top:22px;font-weight:600}
</style>
</head>
<body>

<div class="page-col col-a">
  <section class="hero">
    <div class="photo" role="img" aria-label="Aerial photo of wind turbines above a flat town and farmland"></div>
    <nav class="nav">
      <div class="brand"><i></i>Marrowick</div>
      <div class="nav-links"><span>Home</span><span>About Us</span><span>Our Services</span><span>Products Shop</span><span>News</span></div>
      <div class="lang">EN ˄</div>
      <span class="btn">Let's Talk →</span>
    </nav>
    <h1><span class="l1">Exploring renewable</span><span class="l2">natural energy</span></h1>
    <p>Adipiscing elit, sed do eiusmod tempor incididunt ut labore et dolore magna aliqua. Ut enim ad minim veniam. Natus error sit voluptatem accusantium.</p>
  </section>

  <section class="sources">
    <div class="eyebrow">Renewable sources</div>
    <h2>Empowering future<br>with green energy</h2>
    <div class="source-list">
      <div class="source">
        <div class="ic"><svg width="13" height="13" viewBox="0 0 24 24" fill="none" stroke="#7fe03a" stroke-width="1.6"><path d="M4 14h16l-2-6H6z"/><path d="M12 8v6M8 8l-1 6M16 8l1 6M12 14v6M8 20h8M12 2v3M5 4l2 2M19 4l-2 2"/></svg></div>
        <h3>Solar panels</h3>
        <p>Consectetur adipiscing elit, sed do eiusm od tempor incididunt ut labore.</p>
        <div class="arr">→</div>
      </div>
      <div class="source">
        <div class="ic"><svg width="13" height="13" viewBox="0 0 24 24" fill="none" stroke="#7fe03a" stroke-width="1.6"><path d="M9 3c3 4 5 7 5 10a5 5 0 0 1-10 0c0-3 2-6 5-10z"/><path d="M18 9v11M15 20h6"/></svg></div>
        <h3>Hydropower</h3>
        <p>Consectetur adipiscing elit, sed do eiusm od tempor incididunt ut labore.</p>
        <div class="arr">→</div>
      </div>
      <div class="source">
        <div class="ic"><svg width="13" height="13" viewBox="0 0 24 24" fill="none" stroke="#7fe03a" stroke-width="1.6"><circle cx="10" cy="8" r="1.5"/><path d="M10 6.5V2M11.3 8.8l4 2.4M8.7 8.8l-4 2.4M10 9.5V22M16 14v8M14 22h6"/></svg></div>
        <h3>Windmills</h3>
        <p>Consectetur adipiscing elit, sed do eiusm od tempor incididunt ut labore.</p>
        <div class="arr">→</div>
      </div>
    </div>
    <div class="partners">
      <span>NORVELT</span><span>Cobrano</span><span>Haldrin</span><span>Wexford</span>
      <span>tamsell</span><span>Routa</span><span>Orlan</span><span>QUADRIX</span>
    </div>
  </section>

  <section class="growth">
    <div class="photo worker" role="img" aria-label="Engineer in hard hat and hi-vis vest beside solar panels and a wind turbine"></div>
    <div class="copy">
      <h2>Green solutions for<br>energy growth</h2>
      <p>Adipiscing elit, sed do eiusmod tempor incididunt ut labore et dolore magna aliqua. Ut enim ad minim veniam natus error sit voluptatem accusantium doloremque laudantium.</p>
      <p>Veritatis et quasi architecto beatae vitae dicta sunt explicabo. Nemo enim ipsam voluptatem quia voluptas.</p>
      <span class="btn">About Us</span>
    </div>
    <div class="photo mill" role="img" aria-label="Old stone windmill with lattice sails"></div>
    <div class="mark"><i></i>Marrowick</div>
    <div class="prev">←</div>
    <div class="quote">
      <div class="avatar" role="img" aria-label="Customer portrait"></div>
      <p>Sed ut perspiciatis unde omnis iste natus ut perspic iatis unde omnis iste perspiciatis ut rspiciatis unde omnis iste natus. Sed ut perspiciatis. Consectetur adipiscing elit, sed do eiusm onsectetur adipiscing elit.</p>
      <div class="q">”</div>
      <div class="who">Tomas Reeve</div>
      <div class="role">Local rep</div>
      <div class="dots"><i class="on"></i><i></i><i></i></div>
    </div>
  </section>

  <section class="banner">
    <div class="photo" role="img" aria-label="Row of brick houses with solar panels on the roofs under a blue sky"></div>
    <div class="inner">
      <div class="eyebrow">Our services</div>
      <h2>Transforming sunlight into<br>renewable energy</h2>
      <span class="btn">Our Services</span>
    </div>
  </section>
</div>

<div class="page-col col-b">
  <section class="offer">
    <div class="eyebrow">Price table</div>
    <h2>We offer modern<br>energy solutions</h2>
    <div class="sub">Curabitur tellus leo, euismod sit amet gravida at, egestas sed commodo.</div>
    <div class="plans">
      <div class="plan"><div class="name">Silver Pack</div><div class="price">$35.00</div><div class="per">Per month</div><div class="txt">Sed ut perspiciatis unde omnis iste natus ut perspic iatis.</div><div class="get">Get Now</div></div>
      <div class="plan mid"><div class="name">Gold Pack</div><div class="price">$55.00</div><div class="per">Per month</div><div class="rule"></div><div class="txt">Sed ut perspiciatis unde omnis iste natus ut perspic iatis.</div><div class="get">Get Now</div></div>
      <div class="plan"><div class="name">Platinum Pack</div><div class="price">$75.00</div><div class="per">Per month</div><div class="txt">Sed ut perspiciatis unde omnis iste natus ut perspic iatis.</div><div class="get">Get Now</div></div>
    </div>
    <div class="homes">
      <div class="photo house" role="img" aria-label="Brick house with a solar panel roof"></div>
      <div class="tag">Adipiscing elit,<br>sed doeiusmod<br>incididunt</div>
      <div class="copy">
        <div class="eyebrow">Corporate services</div>
        <h3>Powering homes<br>and businesses</h3>
        <p>Duis aute explicabo. Nemo enim ipsam voluptatem quia voluptas sit aspernatur aut odit aut fugit, sed quia.</p>
        <ul><li><b>01</b>Turbines installation</li><li><b>02</b>Process optimization</li></ul>
        <span class="white">About Us</span>
      </div>
    </div>
  </section>

  <section class="marquee" aria-label="Renewable Energy">
    <div class="band band-dark">le <span class="sq"></span> Renewable <span class="sq"></span> Renewable <span class="sq"></span> Rene</div>
    <div class="band band-lime">rgy <em>✳</em> Energy <em>✳</em> Energy <em>✳</em></div>
  </section>

  <section class="blog">
    <div class="eyebrow">What we do</div>
    <h2>Modern green energy solutions &amp; equipment, crafted with innovation, sustainability, passion and <u>talent</u>.</h2>
    <div class="sig">Jorin Hale<span>Chief engineer</span></div>
    <div class="posts">
      <article class="post"><div class="photo thumb" role="img" aria-label="Wind turbines over green fields"></div><div class="meta">CONSTRUCTION · April 2, 2024 · 0 Comments</div><h4>Investing in renewable energy for tomorrow</h4></article>
      <article class="post"><div class="photo thumb" role="img" aria-label="Top-down view of a wind turbine over brown fields"></div><div class="meta">CONSTRUCTION · April 2, 2024 · 0 Comments</div><h4>Green energy myths busted and explained</h4></article>
      <article class="post"><div class="photo thumb" role="img" aria-label="Wind turbine on open farmland"></div><div class="meta">CONSTRUCTION · April 2, 2024 · 0 Comments</div><h4>How wind turbines provide clean energy</h4></article>
    </div>
    <div class="dots"><i></i><i class="on"></i><i></i></div>
  </section>

  <footer class="footer">
    <div class="social"><i></i><i></i><i></i><i></i></div>
    <h2><span class="dim">Let's work together!<br>Just drop me a line – </span><u>info@marrowick.com</u></h2>
    <small>Marrowick Off-Grid Energy © 2024. All rights reserved.</small>
  </footer>
</div>

</body>
</html>
```